Logo and Business card design!

Welbrook Estates

We are a Property development and real estate company (needs a logo design).

Welbrook estates is based in Sydney Australia and will be dealing with high net worth individuals with a corporate background. The demographic of clients will be relatively youthful and savvy. We do development finance, property development and some portion of property sales

I'd like the 'Welbrook' part of the name to be strength of the title, with 'property' playing a very minor part, perhaps in tiny font somewhere off to the bottom or side or something

Thank you!

Target Market(s)

25-55 years old

Industry/Entity Type

Real Estate Development

Contact Information for Business Card

Please arrange this information as you see fit

Leon Brightwater
Managing Director
0417 582 273
leon@welbrookestates-example.com.au
www.welbrookestates-example.com.au

Logo Text

Welbrook estates

Font styles to use
Serif

Colors

Designer to choose colors to be used in the design.

Requirements
Must have
• PLEASE VIEW THE UPLOADED IMAGES AND EXAMPLES
• And please put 'property' in small letters at the bottom or to the side. I want it to play a minimalist role, with 'WELBROOK' being the feature
• Colours! Please make sure theyre mostly grey and white with possibly some other dark blue and maybe dark grey
Nice to have
• Please feel free to use whatever colors you like, the suggested colors are something I selected momentarily and dont necessarily reflect strict guidelines
Should not have
• NO pictures or shapes of houses. I dont want the logo design to be so literal in its imagery

```html
<!DOCTYPE html>
<html lang="en">
<head>
<meta charset="utf-8">
<title>Welbrook Estates — Business Card</title>
<link rel="stylesheet" href="https://fonts.googleapis.com/css2?family=Bebas+Neue&family=Open+Sans:wght@300;400&family=Raleway:wght@300&display=swap">
<style>
  :root {
    --page: #e4e4e4;
    --card-dark: #2f2f2f;
    --card-light: #f7f7f7;
    --ink-light: #f2f2f2;
    --ink-dark: #222222;
    --ink-muted: #555555;
    --rule-dark: #6a6a6a;
    --rule-light: #444444;
  }
  * { box-sizing: border-box; margin: 0; padding: 0; }
  html, body { width: 1200px; height: 904px; overflow: hidden; }
  body {
    background: var(--page);
    display: flex;
    flex-direction: column;
    align-items: center;
    justify-content: center;
    gap: 40px;
  }
  .card {
    width: 700px;
    height: 400px;
    position: relative;
    box-shadow: 0 6px 18px rgba(0,0,0,0.18);
  }
  /* Front */
  .card--front {
    background: var(--card-dark);
    display: flex;
    align-items: center;
    justify-content: center;
    gap: 26px;
  }
  .brand-square {
    width: 38px;
    height: 38px;
    background: var(--ink-light);
  }
  .brand-name {
    font-family: "Raleway", sans-serif;
    font-weight: 300;
    color: var(--ink-light);
    text-align: center;
  }
  .brand-name__main {
    display: block;
    font-size: 40px;
    letter-spacing: 0.28em;
    margin-right: -0.28em;
  }
  .brand-name__sub {
    display: block;
    font-size: 11px;
    letter-spacing: 0.45em;
    margin-top: 4px;
  }
  /* Back */
  .card--back {
    background: linear-gradient(135deg, #ffffff 0%, var(--card-light) 60%, #ececec 100%);
    display: flex;
    align-items: center;
    padding-left: 70px;
  }
  .person {
    text-align: right;
    margin-right: 22px;
  }
  .person__name {
    font-family: "Bebas Neue", sans-serif;
    font-size: 50px;
    line-height: 1;
    color: var(--ink-dark);
  }
  .person__title {
    font-family: "Open Sans", sans-serif;
    font-weight: 300;
    font-size: 15px;
    color: var(--ink-muted);
    margin-top: 2px;
  }
  .divider {
    width: 1px;
    height: 84px;
    background: var(--rule-light);
    margin-right: 18px;
  }
  .contact { list-style: none; }
  .contact__item {
    display: flex;
    align-items: center;
    gap: 9px;
    font-family: "Open Sans", sans-serif;
    font-weight: 400;
    font-size: 13px;
    color: var(--ink-muted);
    line-height: 22px;
  }
  .contact__icon { width: 11px; height: 11px; flex: none; }
  .brand-corner {
    position: absolute;
    right: 40px;
    bottom: 120px;
    font-family: "Raleway", sans-serif;
    font-weight: 300;
    font-size: 16px;
    letter-spacing: 0.2em;
    color: var(--ink-dark);
  }
</style>
</head>
<body>
  <section class="card card--front" aria-label="Card front">
    <div class="brand-square"></div>
    <div class="brand-name">
      <span class="brand-name__main">WELBROOK</span>
      <span class="brand-name__sub">ESTATES</span>
    </div>
  </section>

  <section class="card card--back" aria-label="Card back">
    <div class="person">
      <h1 class="person__name">Leon Brightwater</h1>
      <p class="person__title">Managing Director</p>
    </div>
    <div class="divider"></div>
    <ul class="contact">
      <li class="contact__item">
        <svg class="contact__icon" viewBox="0 0 12 12"><path d="M2.5 1 L4.5 1 L5.3 3.5 L4 4.6 Q5.2 7 7.4 8 L8.5 6.7 L11 7.5 L11 9.5 Q10.5 11 9 11 Q2 10 1 3 Q1 1.5 2.5 1 Z" fill="#444"/></svg>
        0417 582 273
      </li>
      <li class="contact__item">
        <svg class="contact__icon" viewBox="0 0 12 12"><rect x="0.5" y="2" width="11" height="8" rx="1" fill="#444"/><path d="M1 2.6 L6 6.5 L11 2.6" stroke="#fff" stroke-width="1" fill="none"/></svg>
        leon@welbrookestates-example.com.au
      </li>
      <li class="contact__item">
        <svg class="contact__icon" viewBox="0 0 12 12"><circle cx="6" cy="6" r="5.2" fill="none" stroke="#444" stroke-width="1.2"/><ellipse cx="6" cy="6" rx="2.2" ry="5.2" fill="none" stroke="#444" stroke-width="1"/><path d="M1 6 H11" stroke="#444" stroke-width="1"/></svg>
        www.welbrookestates-example.com.au
      </li>
    </ul>
    <div class="brand-corner">WELBROOK</div>
  </section>
</body>
</html>
```